Brovanta Business Card Design

Primarily a Real Estate Investment company but also invests in other business ventures.
Updates

The attachments have been uploaded to give you a better perspective on what I'm looking for. Please pay close attention to the Lark Stage Creations card as a sample.Thank you.

Target Market(s)

Upper escalante individuals that would like to purchase real estate

Industry/Entity Type

Business

Contact Information for Business Card

Brovanta Holdings LLC, Danela R. Hartwick, CEO/MBA, 310-555-0147, Danela4816@mailbrook.example

Colors
0455a3
ffffff

Requirements
Must have
• Majority of card color MUST be Black ----- Like pictures 2&3
(pic4) Raised silver foil "B" to start the Brovanta name on the card.
(pic3) Love the whole layout, round edges, placement of contact info. {It is clean and elegant}
(pic1) Matte & Gloss backing
(pic2) Blue color (maybe the remainder of company name to make the card have pop of color).
Nice to have
• Silver foil siding

```html
<!DOCTYPE html>
<html lang="en">
<head>
<meta charset="utf-8">
<title>Brovanta Holdings LLC – Business Card</title>
<link rel="stylesheet" href="https://fonts.googleapis.com/css2?family=Dancing+Script:wght@500&family=Lato:ital,wght@0,400;1,900&display=swap">
<style>
  :root {
    --page-bg: #e6e4e1;
    --card-black: #111111;
    --card-black-edge: #262626;
    --card-white: #ffffff;
    --brand-blue: #0455a3;
    --ink-grey: #4a4a4a;
    --foil: #f2f2f2;
  }
  * { box-sizing: border-box; margin: 0; padding: 0; }
  html, body { width: 1200px; height: 1024px; overflow: hidden; }
  body {
    background: var(--page-bg);
    display: flex;
    flex-direction: column;
    align-items: center;
    justify-content: center;
    gap: 44px;
  }
  .card {
    width: 700px;
    height: 400px;
    border-radius: 22px;
    position: relative;
    box-shadow: 0 10px 28px rgba(0,0,0,0.18);
    overflow: hidden;
  }
  /* Front */
  .card-front {
    background: linear-gradient(135deg, var(--card-black-edge) 0%, var(--card-black) 55%, #050505 100%);
  }
  .brand-mark {
    position: absolute;
    left: 224px;
    top: 74px;
    width: 150px;
    height: 150px;
  }
  .brand-name {
    position: absolute;
    left: 200px;
    top: 252px;
    font-family: "Dancing Script", cursive;
    font-weight: 500;
    font-size: 44px;
    color: var(--foil);
    letter-spacing: 0.5px;
    white-space: nowrap;
  }
  /* Back */
  .card-back {
    background: var(--card-white);
    border: 1px solid #d8d8d8;
  }
  .contact {
    position: absolute;
    left: 300px;
    top: 118px;
    font-family: "Lato", sans-serif;
  }
  .contact-name {
    font-style: italic;
    font-weight: 900;
    font-size: 30px;
    color: var(--brand-blue);
    letter-spacing: 0.5px;
  }
  .contact-title {
    margin-top: 4px;
    font-size: 15px;
    color: var(--ink-grey);
    letter-spacing: 1px;
  }
  .contact-lines {
    margin-top: 34px;
    list-style: none;
    font-size: 16px;
    color: var(--ink-grey);
    line-height: 1.9;
  }
</style>
</head>
<body>
  <section class="card card-front" aria-label="Business card front">
    <svg class="brand-mark" viewBox="0 0 150 150" aria-hidden="true">
      <circle cx="75" cy="75" r="66" fill="none" stroke="var(--foil)" stroke-width="7"/>
    </svg>
    <p class="brand-name">Brovanta Holdings LLC</p>
  </section>

  <section class="card card-back" aria-label="Business card back">
    <div class="contact">
      <h1 class="contact-name">Danela R. Hartwick</h1>
      <p class="contact-title">CEO/MBA</p>
      <ul class="contact-lines">
        <li>310-555-0147</li>
        <li>Danela4816@mailbrook.example</li>
      </ul>
    </div>
  </section>
</body>
</html>
```